Actors Postcard Design

I need a postcard designed for me. I am an actor, voice over artist and technical adviser for tv, film and videogames. I am open to color ideas. My photos are in black and white so something to make those stand out a bit. Masculine colors like dark blue etc..I have seen some of your designs with 3 photos which I liked. Perhaps a 2-3 photo scheme. Back of postcard to contain my resume. Want it to look professional and not cartoonish (since I mentioned video games). Front to have photos and job title and contact info

Please take my color direction lightly, I am open to all color schemes. light or dark. You are the professionals. Am looking forward to seeing what all of you come up with. Thanks

Tv

```html
<!DOCTYPE html>
<html lang="en">
<head>
<meta charset="utf-8">
<title>Tomasz Walenski – Actor Postcard</title>
<link href="https://fonts.googleapis.com/css2?family=Montserrat:ital,wght@0,300;0,400;0,600;0,700;1,400&display=swap" rel="stylesheet">
<style>
  :root {
    --paper: #ffffff;
    --ink-strong: #3d3d3d;
    --ink-body: #6b6b6b;
    --ink-label: #4a4a4a;
    --rule: #cfcfcf;
    --photo-dark: #4e4e4e;
    --photo-mid: #8a8a8a;
    --photo-light: #b9b9b9;
  }
  * { box-sizing: border-box; margin: 0; padding: 0; }
  html, body { width: 1200px; height: 948px; overflow: hidden; background: var(--paper); }
  body { font-family: "Montserrat", Arial, sans-serif; color: var(--ink-body); }
  .postcard { position: relative; width: 1200px; height: 948px; background: var(--paper); }

  .actor-name {
    position: absolute; right: 58px; top: 40px;
    font-size: 30px; letter-spacing: 0.5px; color: var(--ink-strong); font-weight: 300;
  }
  .actor-name strong { font-weight: 700; }

  .headshot {
    position: absolute; top: 109px; height: 293px;
    background: radial-gradient(ellipse at 50% 55%, var(--photo-light) 0%, var(--photo-mid) 45%, var(--photo-dark) 100%);
  }
  .headshot--one { left: 0; width: 383px; background: radial-gradient(ellipse at 60% 55%, #c4c4c4 0%, #9a9a9a 50%, #6f6f6f 100%); }
  .headshot--two { left: 397px; width: 406px; }
  .headshot--three { left: 819px; width: 381px; }

  .stats-bar {
    position: absolute; top: 452px; left: 60px; right: 30px;
    display: flex; align-items: baseline; font-size: 18px; color: var(--ink-body); font-weight: 300;
  }
  .stat { margin-right: 26px; }
  .stat b { font-weight: 700; color: var(--ink-label); }
  .stats-divider { width: 1px; height: 22px; background: var(--rule); margin: 0 36px 0 10px; align-self: center; }
  .contact-email { font-weight: 700; color: var(--ink-label); margin-right: 22px; }

  .column { position: absolute; top: 540px; }
  .column--training { left: 63px; width: 480px; }
  .column--advising { left: 642px; width: 520px; top: 530px; }
  .column-divider { position: absolute; left: 563px; top: 541px; width: 2px; height: 350px; background: var(--rule); }

  .section-title { font-size: 30px; font-weight: 600; color: var(--ink-strong); line-height: 1.1; }
  .section-sub { font-size: 19px; font-style: italic; color: #222; margin-top: 2px; }

  .entry-list { list-style: none; font-size: 19px; line-height: 25px; font-weight: 300; color: var(--ink-body); }
  .column--training .entry-list { margin-top: 26px; }
  .subhead { font-size: 19px; font-weight: 700; color: var(--ink-label); margin-top: 24px; line-height: 25px; }
  .body-text { font-size: 19px; line-height: 25px; font-weight: 300; }
  .note-list { list-style: none; font-size: 17px; font-style: italic; line-height: 22px; margin-top: 16px; font-weight: 300; }

  .column--advising .subhead:first-of-type { margin-top: 26px; }
  .skills-text { font-size: 17px; line-height: 24.5px; font-weight: 400; }
</style>
</head>
<body>
<main class="postcard">
  <h1 class="actor-name"><strong>TOMASZ</strong> "TOM" WALENSKI</h1>

  <div class="headshot headshot--one" role="img" aria-label="Black and white headshot of the actor in a puffer jacket, misty forest behind"></div>
  <div class="headshot headshot--two" role="img" aria-label="Black and white headshot of the actor in a collared shirt, leafy background"></div>
  <div class="headshot headshot--three" role="img" aria-label="Black and white headshot of the actor in a plaid shirt, trees behind"></div>

  <div class="stats-bar">
    <span class="stat"><b>Height:</b> 6'0"</span>
    <span class="stat"><b>Weight:</b> 180</span>
    <span class="stat"><b>Hair:</b> Blond</span>
    <span class="stat"><b>Eyes:</b> Green</span>
    <span class="stats-divider"></span>
    <span class="contact-email">tomwalenski@mailbox.net</span>
    <span class="contact-phone">503-555-0148</span>
  </div>

  <section class="column column--training">
    <h2 class="section-title">Training/Experience</h2>
    <p class="section-sub">Acting</p>
    <ul class="entry-list">
      <li>Marla Hayden Acting School - 1.5 yrs</li>
      <li>Screen Actors Lab – On Camera 2yrs</li>
      <li>Highland Acting Coach – 5 day intensive</li>
    </ul>
    <h3 class="subhead">Voice Over</h3>
    <p class="body-text">Vox Studio – Evening Conservatory<br>(commercial, narration, etc…)</p>
    <ul class="note-list">
      <li>- Adv Evening Conservatory</li>
      <li>- 4 day Character Intensive</li>
    </ul>
  </section>

  <div class="column-divider"></div>

  <section class="column column--advising">
    <h2 class="section-title">Technical Advising</h2>
    <p class="section-sub">Federal Special Agent – 10.5 yrs</p>
    <h3 class="subhead">Extensive Firearms Training <span class="body-text" style="font-weight:300;color:var(--ink-body)">– Federal, Northgate Tactics,</span></h3>
    <p class="body-text">Former Special Ops Members, Army ODA. Defensive Tactics, Breaching, Vehicle Containment, Surveillance, etc…</p>
    <h3 class="subhead">Special Skills</h3>
    <p class="skills-text">15 yrs martial arts (Gung Fu, Judo, Tai Chi, Kenjutsu), EMT, Personal Trainer, Scuba, Snowboarding, Snowshoeing, Alpine Mountaineering, Archery, Mountainbiking, SUP, Blacksmithing, Carpentry 7yrs. Fluent Polish.</p>
  </section>
</main>
</body>
</html>
```